Creative pkg design 4 our craft cannabis vaporizer cartridges that stands out above the so-so boxes

We need a package design for our full spectrum terpene rich vaporizer cannabis cartridges that complies with DVRB regulations and conveys a modern, colorful, clean, natural feel to a youngish market. Our cannabis is from the northwest (USA) where we appreciate the clean air, mountains, rivers and healthiness of the area. We stress quality, purity & sustainability. Our marijuana farm is also a trout farm and our logo uses triangles to symbolize the mountains. We are printing on a white box and like this as a foundation. Our logo is usually either silver and black (text silver or black with background opposite) but we are open to playing with the colors & affects etc. We want our package to pop and stand out from the rest. Our market is obviously marijuana users that are over 21, somewhat sophisticated and focused on value and quality from an experienced, trustworthy company. The DVRB requires special placement of some text and some symbols. See layout file. There is a lot of text required but we're hoping for a cool image or graphic concept incorporated behind or dispersed throughout. Our company is Copper Meadow Distillates (CMD)
Updates

We are extending the deadline until next Wednesday. We updated the brief and are looking for something a little more creative and colorful. Not quite so serious and conservative

Target Market(s)

marijuana users over 21, somewhat sophisticated, healthy and focused on value and quality from an experienced, trustworthy company

Industry/Entity Type

Cannabis - marijuana

Font styles to use
Sans Serif

Requirements
Must have
• Must have required text as stated in layout attachment
Should not have
• Cannot be cartoonish

```html
<!DOCTYPE html>
<html lang="en">
<head>
<meta charset="utf-8">
<title>Cannabis Extract Cartridge Packaging</title>
<link rel="stylesheet" href="https://fonts.googleapis.com/css2?family=Montserrat:wght@500;700;800&family=Oswald:wght@300;400;700&display=swap">
<style>
  :root{
    --canvas:#ffffff;
    --ink:#1e1e1e;
    --paper:#f2f2f2;
    --white:#ffffff;
    --warn-red:#e0262b;
    --warn-black:#2a2a2a;
    --green-band:#86a024;
    --blue-band:#0a98d8;
  }
  *{margin:0;padding:0;box-sizing:border-box}
  html,body{width:1200px;height:1200px;overflow:hidden;background:var(--canvas)}
  .canvas{position:relative;width:1200px;height:1200px}

  .package{position:absolute;top:210px;width:370px;height:780px;display:flex;box-shadow:0 2px 8px rgba(0,0,0,.12)}
  .package--green{left:190px;
    --band:var(--green-band);
    --scene:linear-gradient(180deg,#d5ddd7 0%,#a9c4b1 22%,#7ea58c 45%,#4f7f4b 70%,#2f5a30 100%);
    --reflection:linear-gradient(180deg,#4a6151 0%,#6d8b76 45%,#a9c3ad 100%);}
  .package--blue{left:640px;
    --band:var(--blue-band);
    --scene:linear-gradient(180deg,#dcdfe2 0%,#b7c8d4 22%,#8fa6b6 45%,#4f7a4c 72%,#2f5a30 100%);
    --reflection:linear-gradient(180deg,#536073 0%,#71849a 45%,#a9bdb8 100%);}

  /* Side panel */
  .side-panel{position:relative;width:80px;height:100%;background:var(--paper);overflow:hidden;font-family:"Oswald",sans-serif;font-weight:300;text-align:center;color:#2a2a2a}
  .side-panel__scene{position:absolute;left:0;top:150px;width:100%;height:290px;background:var(--scene)}
  .side-panel__reflection{position:absolute;left:0;top:520px;width:100%;height:260px;background:var(--reflection)}
  .side-panel__band{position:absolute;left:0;top:440px;width:100%;height:80px;background:var(--band);color:var(--white);font-size:11px;line-height:1.25;display:flex;align-items:center;justify-content:center;padding:0 6px}
  .story{position:absolute;left:4px;right:4px;top:40px;font-size:10px;line-height:1.3}
  .story__title{font-weight:700;font-size:10.5px}
  .story__more{color:rgba(255,255,255,.85);margin-top:4px}
  .story__note{color:var(--white);margin-top:8px}
  .handles{position:absolute;left:0;right:0;top:530px;font-size:9px;font-weight:700;color:var(--white);line-height:1.7}
  .disclaimer{position:absolute;left:4px;right:4px;top:578px;font-size:10px;line-height:1.6;color:var(--white)}

  /* Front panel */
  .front-panel{position:relative;width:290px;height:100%;background:var(--paper);overflow:hidden;font-family:"Montserrat",sans-serif}
  .front-panel__scene{position:absolute;left:0;top:100px;width:100%;height:340px;background:var(--scene)}
  .product-title{position:absolute;left:0;right:0;top:52px;text-align:center;font-weight:800;color:var(--ink);font-size:31px;line-height:1;letter-spacing:.3px}
  .product-title span{display:block}
  .brand-name{position:absolute;left:0;right:0;top:245px;display:flex;align-items:center;justify-content:center;gap:8px}
  .brand-name__dot{width:12px;height:12px;border-radius:50%;background:var(--white)}
  .brand-name__text{font-weight:700;font-size:17px;color:var(--white);text-transform:uppercase;letter-spacing:.5px}
  .ingredients{position:absolute;left:0;right:0;top:372px;text-align:center;font-weight:800;color:var(--white);font-size:19px;line-height:1.35;letter-spacing:.4px}
  .strain-band{position:absolute;left:0;top:440px;width:100%;height:80px;background:var(--band);display:flex;align-items:center;justify-content:center}
  .strain-band__name{font-family:"Oswald",sans-serif;font-weight:700;font-size:42px;color:var(--white);letter-spacing:.5px}
  .potency{position:absolute;left:0;top:520px;width:100%;height:98px;background:var(--paper);padding:14px 38px 0;font-weight:500;font-size:15px;color:var(--ink)}
  .potency__row{display:flex;justify-content:center;border-bottom:1.5px solid var(--ink);padding:3px 0}
  .potency__row:last-child{border-bottom:none}
  .potency__row--split span:first-child{padding-right:16px;border-right:1.5px solid var(--ink);margin-right:16px}
  .front-panel__reflection{position:absolute;left:0;top:618px;width:100%;height:162px;background:var(--reflection)}
  .warning-symbol{position:absolute;left:95px;top:636px}
  .net-weight{position:absolute;left:0;right:0;top:742px;text-align:center;font-weight:800;color:var(--white);font-size:15px}
</style>
</head>
<body>
<div class="canvas">

  <section class="package package--green">
    <aside class="side-panel">
      <div class="side-panel__scene" role="img" aria-label="Forest and mountain landscape illustration"></div>
      <div class="story">
        <p class="story__title">Our story</p>
        <p>We grow small batch cannabis on a spring fed farm beside cold mountain water. Our oils are made in small premium runs and are always 100% cannabis derived.</p>
        <p class="story__more">We're neighbors with a love for nature, purity and sustainability. We are thankful for our clean flowing water, easing our load on local resources.</p>
        <p class="story__note">CMD oils are full spectrum with no additives.</p>
      </div>
      <div class="side-panel__band">You'll taste the difference!</div>
      <div class="side-panel__reflection" role="img" aria-label="Lake reflection of mountains"></div>
      <div class="handles"><p>@CMDISTILL</p><p>@CMFARMS</p></div>
      <p class="disclaimer">This package is not child resistant. This product is not approved by the FDA to treat, cure or prevent any disease.</p>
    </aside>
    <div class="front-panel">
      <div class="front-panel__scene" role="img" aria-label="Forest and mountain landscape illustration"></div>
      <h1 class="product-title"><span>CANNABIS</span><span>EXTRACT</span><span>CARTRIDGE</span></h1>
      <div class="brand-name"><span class="brand-name__dot"></span><p class="brand-name__text">Copper Meadow Farms</p></div>
      <p class="ingredients">Cannabis&nbsp; Derivved<br>Terpenes + Distillate</p>
      <div class="strain-band"><p class="strain-band__name">STRAIN NAME</p></div>
      <div class="potency">
        <div class="potency__row potency__row--split"><span>THC: xx%</span><span>CBD: xx%</span></div>
        <div class="potency__row"><span>Terpenes: xx%</span></div>
        <div class="potency__row"><span>Total Cannabinoids: xx%</span></div>
      </div>
      <div class="front-panel__reflection" role="img" aria-label="Lake reflection of mountains"></div>
      <svg class="warning-symbol" width="100" height="72" viewBox="0 0 100 72" aria-label="Required warning symbol">
        <rect x="0" y="0" width="100" height="72" rx="8" fill="var(--warn-black)"/>
        <rect x="36" y="6" width="58" height="60" rx="3" fill="var(--warn-red)"/>
        <rect x="12" y="10" width="12" height="34" rx="3" fill="#ffffff"/>
        <circle cx="18" cy="56" r="7" fill="#ffffff"/>
      </svg>
      <p class="net-weight">Net Weight: 1 G (0.035 OZ)</p>
    </div>
  </section>

  <section class="package package--blue">
    <aside class="side-panel">
      <div class="side-panel__scene" role="img" aria-label="Forest and mountain landscape illustration"></div>
      <div class="story">
        <p class="story__title">Our story</p>
        <p>We grow small batch cannabis on a spring fed farm beside cold mountain water. Our oils are made in small premium runs and are always 100% cannabis derived.</p>
        <p class="story__more">We're neighbors with a love for nature, purity and sustainability. We are thankful for our clean flowing water, easing our load on local resources.</p>
        <p class="story__note">CMD oils are full spectrum with no additives.</p>
      </div>
      <div class="side-panel__band">You'll taste the difference!</div>
      <div class="side-panel__reflection" role="img" aria-label="Lake reflection of mountains"></div>
      <div class="handles"><p>@CMDISTILL</p><p>@CMFARMS</p></div>
      <p class="disclaimer">This package is not child resistant. This product is not approved by the FDA to treat, cure or prevent any disease.</p>
    </aside>
    <div class="front-panel">
      <div class="front-panel__scene" role="img" aria-label="Forest and mountain landscape illustration"></div>
      <h1 class="product-title"><span>CANNABIS</span><span>EXTRACT</span><span>CARTRIDGE</span></h1>
      <div class="brand-name"><span class="brand-name__dot"></span><p class="brand-name__text">Copper Meadow Farms</p></div>
      <p class="ingredients">Cannabis&nbsp; Derivved<br>Terpenes + Distillate</p>
      <div class="strain-band"><p class="strain-band__name">STRAIN NAME</p></div>
      <div class="potency">
        <div class="potency__row potency__row--split"><span>THC: xx%</span><span>CBD: xx%</span></div>
        <div class="potency__row"><span>Terpenes: xx%</span></div>
        <div class="potency__row"><span>Total Cannabinoids: xx%</span></div>
      </div>
      <div class="front-panel__reflection" role="img" aria-label="Lake reflection of mountains"></div>
      <svg class="warning-symbol" width="100" height="72" viewBox="0 0 100 72" aria-label="Required warning symbol">
        <rect x="0" y="0" width="100" height="72" rx="8" fill="var(--warn-black)"/>
        <rect x="36" y="6" width="58" height="60" rx="3" fill="var(--warn-red)"/>
        <rect x="12" y="10" width="12" height="34" rx="3" fill="#ffffff"/>
        <circle cx="18" cy="56" r="7" fill="#ffffff"/>
      </svg>
      <p class="net-weight">Net Weight: 1 G (0.035 OZ)</p>
    </div>
  </section>

</div>
</body>
</html>
```